Water ATM Card

Need a design for water ATM cards. Size of card is 3.375 x 2.125 inch
On the Front include the Cedar Brook Logo.
Bottom right corner should have Price $100
On the Back
This card is to be used to access water refills at any Cedar Brook Water Vending Machines.
Please contact (869) 415 2983 or (869) 238 4617 or email clearflowhub@mailbox-example.com for any assistance or recharging of card.

```html
<!DOCTYPE html>
<html lang="en">
<head>
<meta charset="utf-8">
<title>Cedar Brook Water Card</title>
<link href="https://fonts.googleapis.com/css2?family=Montserrat:wght@800&family=Antonio:wght@100&display=swap" rel="stylesheet">
<style>
  :root {
    --bg: #222222;
    --card: #1b1b1b;
    --edge: #2fa847;
    --brand-blue: #0b78c2;
    --band-light: #7cc04a;
    --band-dark: #1f9e48;
    --band-rim: #2a7fd0;
    --price: #ffffff;
  }
  * { margin: 0; padding: 0; box-sizing: border-box; }
  html, body {
    width: 1200px; height: 711px; overflow: hidden;
    background: var(--bg);
  }
  .canvas {
    width: 1200px; height: 711px;
    display: flex; align-items: center; justify-content: center; gap: 60px;
  }
  .card {
    position: relative;
    width: 500px; height: 315px;
    background: var(--card);
    border-radius: 22px;
    border: 3px solid var(--edge);
    box-shadow: 0 14px 30px rgba(0,0,0,0.55);
    overflow: hidden;
  }
  .brand {
    position: absolute;
    left: 0; right: 0; top: 118px;
    display: flex; align-items: center; justify-content: center; gap: 14px;
  }
  .brand-dot {
    width: 22px; height: 22px; border-radius: 50%;
    background: var(--brand-blue);
  }
  .brand-name {
    font-family: "Montserrat", sans-serif;
    font-weight: 800;
    font-size: 44px;
    letter-spacing: 1px;
    text-transform: uppercase;
    color: var(--brand-blue);
  }
  .price-band {
    position: absolute; left: 0; top: 0;
    width: 100%; height: 100%;
  }
  .price-label {
    position: absolute;
    right: 70px; bottom: 46px;
    font-family: "Antonio", sans-serif;
    font-weight: 100;
    font-size: 40px;
    color: var(--price);
    transform: rotate(-14deg);
    transform-origin: right bottom;
    letter-spacing: 1px;
  }
  .card--front .brand { top: 92px; }
</style>
</head>
<body>
<main class="canvas">
  <section class="card card--plain" aria-label="Cedar Brook card">
    <div class="brand">
      <span class="brand-dot"></span>
      <span class="brand-name">Cedar Brook</span>
    </div>
  </section>

  <section class="card card--front" aria-label="Cedar Brook card front with price">
    <svg class="price-band" viewBox="0 0 494 309" preserveAspectRatio="none" aria-hidden="true">
      <defs>
        <linearGradient id="bandFill" x1="0" y1="0" x2="0.3" y2="1">
          <stop offset="0" stop-color="var(--band-light)"/>
          <stop offset="1" stop-color="var(--band-dark)"/>
        </linearGradient>
      </defs>
      <path d="M185 309 Q290 178 494 168 L494 309 Z" fill="url(#bandFill)"/>
      <path d="M185 309 Q290 178 494 168" fill="none" stroke="var(--band-rim)" stroke-width="4"/>
    </svg>
    <div class="brand">
      <span class="brand-dot"></span>
      <span class="brand-name">Cedar Brook</span>
    </div>
    <p class="price-label">PRICE $100</p>
  </section>
</main>
</body>
</html>
```